Change color scheme of existing flyers

Hello! We recently re-branded our company with an awesome logo from Sketch Vault.
We changed our color scheme from Orange/Black to Red/Blue/Gray as you will see in the attachments.
We have a 4 page flyer that we need to incorporate the new colors into and have them look nice.
The pages are bound so the colors must flow well from page to page.
Please don't just replace logo, change orange to red, and submit. I designed the current flyers and can do that in 10 minutes. I'm looking for some great ideas to implement and make the flyers look as good as the new logo.:-)
This is a fun project but I have no time at the moment so I need your help.
I am attaching the old pdf versions and the new logo options for consideration.
Look forward to some creative input. Thanks!

Target Market(s)

Manufacturers

Industry/Entity Type

It Company

Requirements
Must have
• Must have flow from page to page similar to old black/orange version
Nice to have
• We like the current configuration but are open to new designs also

```html
<!DOCTYPE html>
<html lang="en">
<head>
<meta charset="utf-8">
<title>Ductboard Products Flyer</title>
<link rel="stylesheet" href="https://fonts.googleapis.com/css2?family=Arimo:wght@400;700&display=swap">
<style>
  :root {
    --red: #e3001b;
    --red-dark: #b50014;
    --ink: #111111;
    --paper: #ffffff;
    --frame: #000000;
    --backdrop: #2a2a2a;
    --backdrop-light: #3a3a3a;
    --metal-light: #e4e6ea;
    --metal-mid: #a9adb6;
    --metal-dark: #6f737c;
  }
  * { box-sizing: border-box; margin: 0; padding: 0; }
  html, body { width: 957px; height: 1200px; overflow: hidden; }
  body {
    position: relative;
    font-family: "Arimo", Arial, sans-serif;
    color: var(--ink);
    background: linear-gradient(180deg, var(--backdrop-light) 0%, var(--backdrop) 40%, #1f1f1f 100%);
  }
  .top-swoosh { position: absolute; left: 0; top: 0; width: 957px; height: 200px; }
  .row-frame { position: absolute; left: 53px; width: 876px; background: var(--frame); }
  .frame-top { top: 68px; height: 470px; }
  .frame-bottom { top: 598px; height: 511px; }

  .panel {
    position: absolute;
    background: var(--paper);
    padding: 8px 8px 0 8px;
    display: flex; flex-direction: column;
  }
  .row-1 { top: 76px; height: 456px; }
  .row-2 { top: 606px; height: 496px; }
  .col-1 { left: 59px; width: 282px; }
  .col-2 { left: 345px; width: 284px; }
  .col-3 { left: 633px; width: 290px; }

  .panel-title {
    font-size: 20px; font-weight: 400; color: var(--red);
    letter-spacing: -0.2px; white-space: nowrap; line-height: 24px;
  }
  .panel-title strong { font-weight: 700; }

  .product-shot {
    align-self: center;
    margin: 14px 0 10px;
    width: 158px; height: 122px;
    background: linear-gradient(135deg, var(--metal-light) 0%, var(--metal-mid) 55%, var(--metal-dark) 100%);
    border-radius: 3px;
  }
  .shot-cube { width: 138px; height: 134px; margin-top: 16px; }
  .shot-supply { width: 130px; height: 104px; margin-top: 36px; margin-bottom: 18px; }
  .shot-return { width: 170px; height: 72px; margin-top: 48px; margin-bottom: 40px; }

  .features {
    list-style: none;
    padding-left: 30px;
    font-size: 13px; line-height: 18.5px;
    margin-bottom: 14px;
  }

  .rating { font-size: 17px; font-weight: 700; line-height: 18px; margin-top: 4px; }
  .spec {
    width: 100%;
    border-collapse: collapse;
    font-size: 10.5px; line-height: 12px;
    margin-bottom: 10px;
  }
  .spec th { font-weight: 700; text-align: left; }
  .spec td, .spec th { padding: 0; white-space: nowrap; }
  .spec .num { text-align: center; width: 23px; }
  .spec .part { width: 78px; }

  .footer-band {
    position: absolute; left: 0; top: 1122px; width: 957px; height: 58px;
    background: linear-gradient(180deg, var(--red) 0%, var(--red-dark) 100%);
    display: flex; align-items: center; justify-content: center; gap: 14px;
    color: var(--paper); font-size: 19px;
  }
  .footer-band .sep { width: 1px; height: 16px; background: var(--paper); }
  .footer-rule { position: absolute; left: 0; top: 1182px; width: 957px; height: 4px; background: var(--paper); }
  .footer-base { position: absolute; left: 0; top: 1186px; width: 957px; height: 14px; background: #2c2c2c; }
</style>
</head>
<body>
  <svg class="top-swoosh" viewBox="0 0 957 200" aria-hidden="true">
    <rect width="957" height="200" fill="#ffffff"/>
    <path d="M0 0 H560 C380 20 180 80 60 200 H0 Z" fill="#e3001b"/>
    <path d="M60 200 C230 110 470 70 957 62 V200 Z" fill="#333333"/>
  </svg>

  <div class="row-frame frame-top"></div>
  <div class="row-frame frame-bottom"></div>

  <section class="panel row-1 col-1">
    <h2 class="panel-title">Ductboard <strong>Triangle Boxes</strong></h2>
    <div class="product-shot" role="img" aria-label="Photo of a foil-faced ductboard triangle box with sides labelled A to D"></div>
    <ul class="features">
      <li>R6 or R8 Ductboard</li>
      <li>Assembled (Unassembled available)</li>
      <li>Seams taped with Quellmark UL181</li>
      <li>Staples used on all staple flaps</li>
      <li>Typical Bundles of 6</li>
    </ul>
    <h3 class="rating">R6</h3>
    <table class="spec">
      <tr><th class="part">Part#</th><th>Description</th><th class="num">A</th><th class="num">B</th><th class="num">C</th><th class="num">D</th></tr>
      <tr><td>30-T10A</td><td>Triangle Box-1</td><td class="num">15</td><td class="num">15</td><td class="num">15</td><td class="num">12</td></tr>
      <tr><td>30-T20A</td><td>Triangle Box-2</td><td class="num">15</td><td class="num">15</td><td class="num">15</td><td class="num">15</td></tr>
      <tr><td>30-T30A</td><td>Triangle Box-3</td><td class="num">19</td><td class="num">19</td><td class="num">19</td><td class="num">18</td></tr>
      <tr><td>30-T40A</td><td>Triangle Box-4</td><td class="num">19</td><td class="num">19</td><td class="num">19</td><td class="num">23</td></tr>
    </table>
    <h3 class="rating">R8</h3>
    <table class="spec">
      <tr><th class="part">Part#</th><th>Description</th><th class="num">A</th><th class="num">B</th><th class="num">C</th><th class="num">D</th></tr>
      <tr><td>30-T18</td><td>Triangle Box-1 R8</td><td class="num">19</td><td class="num">19</td><td class="num">19</td><td class="num">15</td></tr>
      <tr><td>30-T28</td><td>Triangle Box-2 R8</td><td class="num">19</td><td class="num">19</td><td class="num">19</td><td class="num">20</td></tr>
      <tr><td>30-T38</td><td>Triangle Box-3 R8</td><td class="num">21</td><td class="num">21</td><td class="num">21</td><td class="num">23</td></tr>
    </table>
  </section>

  <section class="panel row-1 col-2">
    <h2 class="panel-title">Ductboard <strong>Reducer Boxes</strong></h2>
    <div class="product-shot" role="img" aria-label="Photo of a foil-faced ductboard reducer box with sides labelled A to D"></div>
    <ul class="features">
      <li>R6 or R8 Ductboard</li>
      <li>Assembled (Unassembled available)</li>
      <li>Seams taped with Quellmark UL181</li>
      <li>Staples used on all staple flaps</li>
      <li>Typical Bundles of 6</li>
    </ul>
    <h3 class="rating">R6</h3>
    <table class="spec">
      <tr><th class="part">Part#</th><th>Description</th><th class="num">A</th><th class="num">B</th><th class="num">C</th><th class="num">D</th></tr>
      <tr><td>30-R10A</td><td>Reducer Box-1</td><td class="num">18</td><td class="num">10</td><td class="num">10</td><td class="num">12</td></tr>
      <tr><td>30-R20A</td><td>Reducer Box-2</td><td class="num">18</td><td class="num">14</td><td class="num">14</td><td class="num">15</td></tr>
      <tr><td>30-R30A</td><td>Reducer Box-3</td><td class="num">18</td><td class="num">14</td><td class="num">14</td><td class="num">23</td></tr>
      <tr><td>30-R40A</td><td>Reducer Box-4</td><td class="num">20</td><td class="num">16</td><td class="num">16</td><td class="num">20</td></tr>
    </table>
    <h3 class="rating">R8</h3>
    <table class="spec">
      <tr><th class="part">Part#</th><th>Description</th><th class="num">A</th><th class="num">B</th><th class="num">C</th><th class="num">D</th></tr>
      <tr><td>30-R18</td><td>Reducer Box-1 R8</td><td class="num">16</td><td class="num">12</td><td class="num">12</td><td class="num">15</td></tr>
      <tr><td>30-R28</td><td>Reducer Box-2 R8</td><td class="num">18</td><td class="num">14</td><td class="num">14</td><td class="num">15</td></tr>
      <tr><td>30-R38</td><td>Reducer Box-3 R8</td><td class="num">20</td><td class="num">16</td><td class="num">16</td><td class="num">20</td></tr>
    </table>
  </section>

  <section class="panel row-1 col-3">
    <h2 class="panel-title">Ductboard <strong>"Cube" Boxes</strong></h2>
    <div class="product-shot shot-cube" role="img" aria-label="Photo of a foil-faced ductboard cube box with sides labelled A to C"></div>
    <ul class="features">
      <li>R6 or R8 Ductboard</li>
      <li>Assembled (Unassembled available)</li>
      <li>Seams taped with Quellmark UL181</li>
      <li>Staples used on all staple flaps</li>
    </ul>
    <h3 class="rating">R6</h3>
    <table class="spec">
      <tr><th class="part">Part#</th><th>Description</th><th class="num">A</th><th class="num">B</th><th class="num">C</th></tr>
      <tr><td>30-CU12</td><td>Cube 12x12 I.D</td><td class="num">15</td><td class="num">15</td><td class="num">15</td></tr>
      <tr><td>30-CU14</td><td>Cube 14x14 I.D</td><td class="num">17</td><td class="num">17</td><td class="num">17</td></tr>
      <tr><td>30-CU16</td><td>Cube 16x16 I.D</td><td class="num">19</td><td class="num">19</td><td class="num">19</td></tr>
      <tr><td>30-CU18</td><td>Cube 18x18 I.D</td><td class="num">21</td><td class="num">21</td><td class="num">21</td></tr>
      <tr><td>30-CU20</td><td>Cube 20x20 I.D</td><td class="num">23</td><td class="num">23</td><td class="num">23</td></tr>
    </table>
    <h3 class="rating">R8</h3>
    <table class="spec">
      <tr><th class="part">Part#</th><th>Description</th><th class="num">A</th><th class="num">B</th><th class="num">C</th></tr>
      <tr><td>30-CU12-R8</td><td>Cube 12x12 I.D R8</td><td class="num">16</td><td class="num">16</td><td class="num">16</td></tr>
      <tr><td>30-CU14-R8</td><td>Cube 14x14 I.D R8</td><td class="num">18</td><td class="num">18</td><td class="num">18</td></tr>
      <tr><td>30-CU16-R8</td><td>Cube 16x16 I.D R8</td><td class="num">20</td><td class="num">20</td><td class="num">20</td></tr>
      <tr><td>30-CU18-R8</td><td>Cube 18x18 I.D R8</td><td class="num">22</td><td class="num">22</td><td class="num">22</td></tr>
      <tr><td>30-CU20-R8</td><td>Cube 20x20 I.D R8</td><td class="num">24</td><td class="num">24</td><td class="num">24</td></tr>
    </table>
  </section>

  <section class="panel row-2 col-1">
    <h2 class="panel-title">Ductboard <strong>Mixing Boxes</strong></h2>
    <div class="product-shot shot-cube" role="img" aria-label="Photo of a foil-faced ductboard mixing box with sides labelled A to C"></div>
    <ul class="features">
      <li>R6 or R8 Ductboard</li>
      <li>Assembled (Unassembled available)</li>
      <li>Seams taped with Quellmark UL181</li>
      <li>Staples used on all staple flaps</li>
    </ul>
    <h3 class="rating">R6</h3>
    <table class="spec">
      <tr><th class="part">Part#</th><th>Description</th><th class="num">A</th><th class="num">B</th><th class="num">C</th></tr>
      <tr><td>30-M12A</td><td>Mix Box 12x12 I.D</td><td class="num">15</td><td class="num">15</td><td class="num">22</td></tr>
      <tr><td>30-M14A</td><td>Mix Box 14x14 I.D</td><td class="num">17</td><td class="num">17</td><td class="num">22</td></tr>
      <tr><td>30-M16A</td><td>Mix Box 16x16 I.D</td><td class="num">19</td><td class="num">19</td><td class="num">22</td></tr>
      <tr><td>30-M18A</td><td>Mix Box 18x18 I.D</td><td class="num">21</td><td class="num">21</td><td class="num">22</td></tr>
      <tr><td>30-M20A</td><td>Mix Box 20x20 I.D</td><td class="num">23</td><td class="num">23</td><td class="num">22</td></tr>
    </table>
    <h3 class="rating">R8</h3>
    <table class="spec">
      <tr><th class="part">Part#</th><th>Description</th><th class="num">A</th><th class="num">B</th><th class="num">C</th></tr>
      <tr><td>30-M12A-R8</td><td>Mix Box 12x12 I.D R8</td><td class="num">16</td><td class="num">16</td><td class="num">22</td></tr>
      <tr><td>30-M14A-R8</td><td>Mix Box 14x14 I.D R8</td><td class="num">18</td><td class="num">18</td><td class="num">22</td></tr>
      <tr><td>30-M16A-R8</td><td>Mix Box 16x16 I.D R8</td><td class="num">20</td><td class="num">20</td><td class="num">22</td></tr>
      <tr><td>30-M18A-R8</td><td>Mix Box 18x18 I.D R8</td><td class="num">22</td><td class="num">22</td><td class="num">22</td></tr>
      <tr><td>30-M20A-R8</td><td>Mix Box 20x20 I.D R8</td><td class="num">24</td><td class="num">24</td><td class="num">22</td></tr>
    </table>
  </section>

  <section class="panel row-2 col-2">
    <h2 class="panel-title">Register Boxes-<strong>Supply</strong></h2>
    <div class="product-shot shot-supply" role="img" aria-label="Photo of a metal supply register box with dimensions labelled A to C"></div>
    <ul class="features">
      <li>R6 or R8 Ductboard</li>
      <li>Fully Assembled</li>
      <li>Seams taped with Quellmark UL181</li>
      <li>Custom Sizes Available</li>
    </ul>
    <h3 class="rating">R6</h3>
    <table class="spec">
      <tr><th class="part">Part#</th><th>Description</th><th class="num">A</th><th class="num">B</th><th class="num">C</th></tr>
      <tr><td>35-0804-11</td><td>Supply Register Box</td><td class="num">08</td><td class="num">04</td><td class="num">11</td></tr>
      <tr><td>35-1006-11</td><td>Supply Register Box</td><td class="num">10</td><td class="num">06</td><td class="num">11</td></tr>
      <tr><td>35-1206-11</td><td>Supply Register Box</td><td class="num">12</td><td class="num">06</td><td class="num">11</td></tr>
      <tr><td>35-1406-11</td><td>Supply Register Box</td><td class="num">14</td><td class="num">06</td><td class="num">11</td></tr>
      <tr><td>35-1408-11</td><td>Supply Register Box</td><td class="num">14</td><td class="num">08</td><td class="num">11</td></tr>
    </table>
    <h3 class="rating">R8</h3>
    <table class="spec">
      <tr><th class="part">Part#</th><th>Description</th><th class="num">A</th><th class="num">B</th><th class="num">C</th></tr>
      <tr><td>35-0804-11-R8</td><td>Supply Register Box</td><td class="num">08</td><td class="num">04</td><td class="num">11</td></tr>
      <tr><td>35-1006-11-R8</td><td>Supply Register Box</td><td class="num">10</td><td class="num">06</td><td class="num">11</td></tr>
      <tr><td>35-1206-11-R8</td><td>Supply Register Box</td><td class="num">12</td><td class="num">06</td><td class="num">11</td></tr>
      <tr><td>35-1406-11-R8</td><td>Supply Register Box</td><td class="num">14</td><td class="num">06</td><td class="num">11</td></tr>
      <tr><td>35-1408-11-R8</td><td>Supply Register Box</td><td class="num">14</td><td class="num">08</td><td class="num">11</td></tr>
    </table>
  </section>

  <section class="panel row-2 col-3">
    <h2 class="panel-title">Register Boxes-<strong>Return</strong></h2>
    <div class="product-shot shot-return" role="img" aria-label="Photo of a metal return register box with dimensions labelled A to C"></div>
    <ul class="features">
      <li>R6 or R8 Ductboard</li>
      <li>Fully Assembled</li>
      <li>Seams taped with Quellmark UL181</li>
      <li>Custom Sizes Available</li>
    </ul>
    <h3 class="rating">R6</h3>
    <table class="spec">
      <tr><th class="part">Part#</th><th>Description</th><th class="num">A</th><th class="num">B</th><th class="num">C</th></tr>
      <tr><td>35-1414-35</td><td>Return Register Box</td><td class="num">14</td><td class="num">14</td><td class="num">04</td></tr>
      <tr><td>35-1616-35</td><td>Return Register Box</td><td class="num">16</td><td class="num">16</td><td class="num">04</td></tr>
      <tr><td>35-1818-35</td><td>Return Register Box</td><td class="num">18</td><td class="num">18</td><td class="num">04</td></tr>
      <tr><td>35-2020-35</td><td>Return Register Box</td><td class="num">20</td><td class="num">20</td><td class="num">04</td></tr>
      <tr><td>35-2424-35</td><td>Return Register Box</td><td class="num">24</td><td class="num">24</td><td class="num">04</td></tr>
    </table>
    <h3 class="rating">R8</h3>
    <table class="spec">
      <tr><th class="part">Part#</th><th>Description</th><th class="num">A</th><th class="num">B</th><th class="num">C</th></tr>
      <tr><td>35-1414-35-R8</td><td>Return Register Box</td><td class="num">14</td><td class="num">14</td><td class="num">04</td></tr>
      <tr><td>35-1616-35-R8</td><td>Return Register Box</td><td class="num">16</td><td class="num">16</td><td class="num">04</td></tr>
      <tr><td>35-1818-35-R8</td><td>Return Register Box</td><td class="num">18</td><td class="num">18</td><td class="num">04</td></tr>
      <tr><td>35-2020-35-R8</td><td>Return Register Box</td><td class="num">20</td><td class="num">20</td><td class="num">04</td></tr>
      <tr><td>35-2424-35-R8</td><td>Return Register Box</td><td class="num">24</td><td class="num">24</td><td class="num">04</td></tr>
    </table>
  </section>

  <nav class="footer-band">
    <span>Security Cages</span><span class="sep"></span>
    <span>Ductboard Projects</span><span class="sep"></span>
    <span>Tank Stands</span><span class="sep"></span>
    <span>Condenser Wall Brackets</span>
  </nav>
  <div class="footer-rule"></div>
  <div class="footer-base"></div>
</body>
</html>
```